Book Cover for Christian book about open-air preaching

The book is about open-air or outdoor preaching. It is for pastors, evangelists, or any Christian who feels called to share the Gospel with crowds outside of the church. The title is "Quiet Meadows" with a subtitle of "A guide for patient gardening in the distant valley". The Bible verse reference for the title is Jeremiah 20:9. Size will be 9" high by 6"wide
Updates

Went on vacation/holiday

Target Market(s)

Christian pastors, missonaries, evangelists

Industry/Entity Type

religous

Requirements
Must have
• Meet Marlowe Indie Print Services guidelines for book covers

```html
<!DOCTYPE html>
<html lang="en">
<head>
<meta charset="UTF-8">
<title>Quiet Meadows — Book Cover</title>
<link href="https://fonts.googleapis.com/css2?family=Cinzel:wght@400&family=Allura&family=Montserrat:wght@600&family=Bebas+Neue&display=swap" rel="stylesheet">
<style>
  :root {
    --page-bg: #2a2a2a;
    --cover-black: #050608;
    --title-blue: #1ea3e6;
    --white: #ffffff;
    --glow-gold: #e0a53a;
    --glow-amber: #b8661c;
    --haze-green: #3c5a3a;
    --stage-warm: #c8792e;
    --stage-blue: #2f5fc8;
  }
  * { margin: 0; padding: 0; box-sizing: border-box; }
  html, body {
    width: 1200px;
    height: 905px;
    overflow: hidden;
    background: var(--page-bg);
  }
  .cover {
    position: absolute;
    left: 313px;
    top: 22px;
    width: 574px;
    height: 861px;
    background: var(--cover-black);
    overflow: hidden;
  }
  .photo-worship {
    position: absolute;
    left: 0; top: 0;
    width: 100%;
    height: 64%;
    background:
      radial-gradient(ellipse 70% 45% at 55% 52%, rgba(240,190,80,0.85) 0%, rgba(200,120,40,0.55) 40%, rgba(0,0,0,0) 75%),
      linear-gradient(180deg, #17291f 0%, var(--haze-green) 18%, #6a6a34 34%, var(--glow-amber) 55%, #3a200c 78%, var(--cover-black) 100%);
  }
  .photo-arena {
    position: absolute;
    left: 0; bottom: 0;
    width: 100%;
    height: 36%;
    background:
      radial-gradient(ellipse 45% 55% at 25% 45%, rgba(200,121,46,0.85) 0%, rgba(120,60,20,0.4) 55%, rgba(0,0,0,0) 85%),
      radial-gradient(ellipse 45% 55% at 78% 45%, rgba(47,95,200,0.85) 0%, rgba(30,50,120,0.4) 55%, rgba(0,0,0,0) 85%),
      linear-gradient(180deg, var(--cover-black) 0%, #120d14 20%, #1a1520 55%, #07070a 100%);
  }
  .title-main {
    position: absolute;
    top: 92px;
    left: 0; right: 0;
    text-align: center;
    font-family: "Cinzel", serif;
    font-size: 72px;
    letter-spacing: 0.2em;
    padding-left: 0.2em;
    color: var(--title-blue);
    line-height: 1;
  }
  .title-script {
    position: absolute;
    top: 160px;
    left: 0; right: 0;
    text-align: center;
    font-family: "Allura", cursive;
    font-size: 104px;
    color: var(--white);
    line-height: 1;
  }
  .subtitle {
    position: absolute;
    top: 555px;
    left: 0; right: 0;
    text-align: center;
    font-family: "Montserrat", sans-serif;
    font-weight: 600;
    font-size: 16px;
    line-height: 1.3;
    text-transform: uppercase;
    color: var(--white);
  }
  .author {
    position: absolute;
    bottom: 42px;
    left: 0; right: 0;
    text-align: center;
    font-family: "Bebas Neue", sans-serif;
    font-size: 52px;
    letter-spacing: 0.22em;
    padding-left: 0.22em;
    color: var(--white);
    line-height: 1;
  }
</style>
</head>
<body>
  <main class="cover">
    <div class="photo-worship" role="img" aria-label="Open Bible glowing above a crowd of worshippers lifting their hands in warm golden light"></div>
    <div class="photo-arena" role="img" aria-label="Packed stadium arena seen from above, lit in warm orange and blue"></div>
    <h1 class="title-main">QUIET</h1>
    <p class="title-script">meadows</p>
    <p class="subtitle">A guide for patient gardening<br>in the distant valley</p>
    <p class="author">Author Name</p>
  </main>
</body>
</html>
```